Presentation Folder Design

We are a young and dynamic lettings agent in London and surround and we are looking for a fresh and stunning design for our A4 presentation folder. Our colors are shades of green. Our logo can be found on http://www.kelworthlets.co.uk

Please read the technical info below. It is very important to comply with the specs.

Thank you!
Updates

The design should contain 3 shades of green and the logo which will be emailed to you, clean lines, discreet skyline representing buildings.

Technical

Requirements
Must have
• Resolution 350 dpi. The resolution changes over 300 dpi are almost imperceptible so do not increase the resolution without need - it does not improve the quality but enlarges the file volume (size) instead.
Artwork dimentions: 521 x 364 mm. Use template for designing. Folders were designed to fit A4 paper. The easiest way is to download already made template. NOTE: Do not change the position of template toward paper sheet.
Color management Please provide your artwork in CMYK palette. Ensure that ALL images, text and other design elements have colors set to CMYK palette and do not contain any RGB or Pantone colors.
Acceptable file types PDF (ver. 1.4 max) PSD CDR (ver. X3 max) TIF JPG
Maximum percentage of the process inks Cannot exceed : 350%. Complaints about artworks with higher ink coverage will not be accepted (so e.g. do not "deep black" using 100+100+100+100% of CMYK colors).
Deep black: In order to obtain rich saturated black use 84%C 74%M 62%Y 100%K.

```html
<!DOCTYPE html>
<html lang="en">
<head>
<meta charset="utf-8">
<title>Kelworth Lettings – Presentation Folder</title>
<link rel="stylesheet" href="https://fonts.googleapis.com/css2?family=Roboto+Condensed:wght@700&display=swap">
<style>
  :root {
    --green-deep: #174a26;
    --green-mid: #2a6a35;
    --green-leaf: #4f9a2c;
    --green-lime: #8fb327;
    --green-pale: #c9d98a;
    --olive: #8c9a1f;
    --olive-light: #b3bd4a;
    --paper: #ffffff;
    --paper-shade: #e9ecee;
    --stage-top: #9fb0ba;
    --stage-bottom: #e4eaee;
  }
  * { margin: 0; padding: 0; box-sizing: border-box; }
  html, body { width: 1200px; height: 857px; overflow: hidden; }
  body {
    background: linear-gradient(180deg, var(--stage-top), var(--stage-bottom));
    font-family: "Roboto Condensed", "Arial Narrow", sans-serif;
  }
  .folder-sheet {
    position: absolute;
    top: 131px;
    width: 420px;
    height: 594px;
    box-shadow: 0 10px 28px rgba(20, 40, 50, .25);
    overflow: hidden;
  }
  .front-cover { left: 150px; }
  .inside-panel { left: 630px; background: var(--paper); }
  .folder-sheet svg { position: absolute; inset: 0; width: 100%; height: 100%; }

  .brand {
    position: absolute;
    left: 24px;
    top: 184px;
    display: flex;
    align-items: center;
    gap: 8px;
    color: var(--green-leaf);
    font-size: 36px;
    font-weight: 700;
    letter-spacing: -0.5px;
    line-height: 1;
  }
  .brand-mark {
    width: 15px;
    height: 15px;
    background: var(--green-lime);
  }
  .section-label {
    position: absolute;
    left: 24px;
    top: 238px;
    padding: 6px 15px 5px;
    background: var(--green-deep);
    color: var(--paper);
    font-size: 18px;
    font-weight: 700;
    letter-spacing: .5px;
    border: 2px solid var(--paper);
    outline: 1px solid var(--green-deep);
  }
</style>
</head>
<body>

<section class="folder-sheet front-cover" aria-label="Folder front cover">
  <svg viewBox="0 0 420 594">
    <defs>
      <linearGradient id="cover-ground" x1="0" y1="0" x2="0" y2="1">
        <stop offset="0" stop-color="var(--green-mid)"/>
        <stop offset="1" stop-color="var(--green-deep)"/>
      </linearGradient>
      <linearGradient id="skyline-tone" x1="0" y1="0" x2="0" y2="1">
        <stop offset="0" stop-color="var(--olive-light)" stop-opacity="0"/>
        <stop offset=".3" stop-color="var(--olive-light)" stop-opacity=".55"/>
        <stop offset=".6" stop-color="var(--olive)" stop-opacity=".95"/>
        <stop offset="1" stop-color="var(--olive)"/>
      </linearGradient>
      <radialGradient id="flourish-glow" cx=".5" cy=".5" r=".5">
        <stop offset="0" stop-color="var(--green-pale)" stop-opacity=".22"/>
        <stop offset=".7" stop-color="var(--green-pale)" stop-opacity=".1"/>
        <stop offset="1" stop-color="var(--green-pale)" stop-opacity="0"/>
      </radialGradient>
    </defs>
    <rect class="cover-ground" width="420" height="594" fill="url(#cover-ground)"/>
    <ellipse class="flourish-top" cx="270" cy="100" rx="150" ry="85" fill="url(#flourish-glow)" role="img" aria-label="Faint calligraphic flourish ornament"/>
    <ellipse class="flourish-bottom" cx="130" cy="540" rx="150" ry="70" fill="url(#flourish-glow)" role="img" aria-label="Faint calligraphic flourish ornament"/>
    <path class="swoosh-lime" d="M0 108 C120 92 230 146 420 232 L420 520 C300 470 150 430 0 472 Z" fill="var(--green-lime)"/>
    <path class="swoosh-pale" d="M0 124 C120 108 230 161 420 248 L420 505 C300 455 150 418 0 457 Z" fill="var(--green-pale)"/>
    <path class="band-white" d="M0 136 C120 122 230 174 420 260 L420 494 C300 444 150 408 0 444 Z" fill="var(--paper)"/>
    <path class="skyline" d="M0 268 C140 262 280 250 420 240 L420 494 C300 444 150 408 0 444 Z" fill="url(#skyline-tone)" role="img" aria-label="City skyline illustration of London buildings in olive green"/>
    <path class="swoosh-leaf" d="M0 472 C150 430 300 470 420 520 L420 538 C300 488 150 452 0 492 Z" fill="var(--green-leaf)"/>
  </svg>
  <div class="brand"><span class="brand-name">Kelworth</span><span class="brand-mark"></span></div>
  <div class="section-label">LETTINGS</div>
</section>

<section class="folder-sheet inside-panel" aria-label="Folder inside with pocket">
  <svg viewBox="0 0 420 594">
    <defs>
      <linearGradient id="inside-shade" x1="0" y1="0" x2="1" y2="0">
        <stop offset="0" stop-color="var(--paper-shade)"/>
        <stop offset=".3" stop-color="var(--paper)"/>
      </linearGradient>
      <linearGradient id="pocket-ground" x1="0" y1="0" x2="0" y2="1">
        <stop offset="0" stop-color="var(--green-mid)"/>
        <stop offset="1" stop-color="var(--green-deep)"/>
      </linearGradient>
      <radialGradient id="pocket-glow" cx=".5" cy=".5" r=".5">
        <stop offset="0" stop-color="var(--green-pale)" stop-opacity=".22"/>
        <stop offset=".7" stop-color="var(--green-pale)" stop-opacity=".1"/>
        <stop offset="1" stop-color="var(--green-pale)" stop-opacity="0"/>
      </radialGradient>
    </defs>
    <rect class="inside-paper" width="420" height="594" fill="url(#inside-shade)"/>
    <path class="pocket-side" d="M300 40 L420 20 L420 594 L300 594 Z" fill="url(#pocket-ground)"/>
    <path class="pocket-front" d="M0 380 L300 360 L300 594 L0 594 Z" fill="url(#pocket-ground)"/>
    <line class="pocket-fold" x1="300" y1="360" x2="300" y2="594" stroke="#0f3a1b" stroke-width="2"/>
    <ellipse class="flourish-pocket-side" cx="360" cy="250" rx="48" ry="180" fill="url(#pocket-glow)" role="img" aria-label="Faint calligraphic flourish ornament"/>
    <ellipse class="flourish-pocket-front" cx="150" cy="480" rx="140" ry="70" fill="url(#pocket-glow)" role="img" aria-label="Faint calligraphic flourish ornament"/>
  </svg>
</section>

</body>
</html>
```